Software allocation system needs a business card design

We need a business card designed for our software platform - www.tolvexa.com.au

At the moment the logo and website is all black and white, we are happy for suggestions on implementing some colour throughout either the logo or business card.

Industry/Entity Type

Software

Font styles to use
Sans Serif

Colors

Designer to choose colors to be used in the design.

```html
<!DOCTYPE html>
<html lang="en">
<head>
<meta charset="utf-8">
<title>Tolvexa Business Card</title>
<link rel="stylesheet" href="https://fonts.googleapis.com/css2?family=Ubuntu:wght@300;400;700&display=swap">
<style>
  :root {
    --bg: #d9d9d9;
    --card-black: #0b0b0b;
    --card-white: #f7f7f5;
    --lime: #8cc63f;
    --ink: #3a3a3a;
    --ink-strong: #1c1c1c;
    --white: #ffffff;
  }
  * { margin: 0; padding: 0; box-sizing: border-box; }
  html, body { width: 1200px; height: 1000px; overflow: hidden; }
  body {
    background: var(--bg);
    font-family: "Ubuntu", sans-serif;
    position: relative;
  }
  .card {
    position: absolute;
    left: 300px;
    width: 600px;
    height: 350px;
    border-radius: 4px;
    overflow: hidden;
    box-shadow: 0 6px 18px rgba(0,0,0,0.18);
  }
  .card-front { top: 90px; background: var(--card-black); }
  .card-back { top: 540px; background: var(--card-white); }

  .brand-name {
    position: absolute;
    top: 50%; left: 0; right: 0;
    transform: translateY(-50%);
    text-align: center;
    color: var(--white);
    font-weight: 300;
    font-size: 52px;
    letter-spacing: 10px;
  }

  .edge-bar { position: absolute; width: 9px; background: var(--lime); }
  .edge-bar-left { left: 0; top: 55px; height: 90px; }
  .edge-bar-right { right: 0; top: 165px; height: 80px; }

  .contact-list {
    position: absolute;
    top: 78px;
    left: 60px;
    width: 250px;
    list-style: none;
  }
  .contact-item {
    display: flex;
    justify-content: flex-end;
    align-items: center;
    gap: 12px;
    margin-bottom: 12px;
  }
  .contact-text {
    text-align: right;
    font-size: 15px;
    line-height: 19px;
    color: var(--ink);
  }
  .contact-icon { width: 22px; height: 22px; flex: none; }

  .person {
    position: absolute;
    top: 104px;
    left: 328px;
  }
  .person-name {
    font-size: 22px;
    font-weight: 700;
    color: var(--ink-strong);
  }
  .person-role {
    font-size: 14px;
    color: var(--ink);
    margin-top: 2px;
  }

  .base-band {
    position: absolute;
    left: 0; right: 0;
    top: 285px;
    height: 45px;
    background: var(--card-black);
  }
  .tagline {
    position: absolute;
    left: 90px;
    top: 262px;
    width: 380px;
    height: 38px;
    border-radius: 19px;
    background: var(--lime);
    border: 3px solid var(--card-white);
    color: var(--white);
    font-size: 14.5px;
    font-weight: 400;
    letter-spacing: 0.3px;
    display: flex;
    align-items: center;
    justify-content: center;
    text-transform: uppercase;
  }
</style>
</head>
<body>

<section class="card card-front">
  <div class="brand-name">TOLVEXA</div>
</section>

<section class="card card-back">
  <span class="edge-bar edge-bar-left"></span>
  <span class="edge-bar edge-bar-right"></span>

  <ul class="contact-list">
    <li class="contact-item">
      <span class="contact-text">+00 31862047</span>
      <svg class="contact-icon" viewBox="0 0 22 22" aria-hidden="true">
        <circle cx="11" cy="11" r="11" fill="#8cc63f"/>
        <path d="M7.4 6.2c.4-.4 1-.4 1.3 0l1.2 1.5c.3.4.3.9 0 1.2l-.7.7c.6 1.3 1.6 2.3 2.9 2.9l.7-.7c.3-.3.8-.3 1.2 0l1.5 1.2c.4.3.4.9 0 1.3l-.8.8c-.7.7-1.8.8-2.7.3-2.2-1.2-4-3-5.2-5.2-.5-.9-.4-2 .3-2.7z" fill="#fff"/>
      </svg>
    </li>
    <li class="contact-item">
      <span class="contact-text">PO Box 712<br>Kirrawee NSW 2232</span>
      <svg class="contact-icon" viewBox="0 0 22 22" aria-hidden="true">
        <circle cx="11" cy="11" r="11" fill="#8cc63f"/>
        <path d="M11 5.5l-5.5 5h1.6v5.5h3v-3.3h1.8v3.3h3v-5.5h1.6z" fill="#fff"/>
      </svg>
    </li>
    <li class="contact-item">
      <span class="contact-text">hello@tolvexa.com.au</span>
      <svg class="contact-icon" viewBox="0 0 22 22" aria-hidden="true">
        <circle cx="11" cy="11" r="11" fill="#8cc63f"/>
        <rect x="6" y="7.5" width="10" height="7" rx="1" fill="#fff"/>
        <path d="M6.3 8l4.7 3.6L15.7 8" fill="none" stroke="#8cc63f" stroke-width="1.1"/>
      </svg>
    </li>
  </ul>

  <div class="person">
    <div class="person-name">PERSON NAME</div>
    <div class="person-role">Designation</div>
  </div>

  <div class="base-band"></div>
  <div class="tagline">Planning &amp; Compliance for Heavy Industry</div>
</section>

</body>
</html>
```